Wedding Ceremony Equipment Hire Business Card

I need a business card design for a new business I created called Altar Outfitters. We hire out Wedding Ceremony equipment and decorations mainly for beach and garden wedding ceremonies that include delivery, set up and dismantle. We do offer DIY Chair Hire as well.
I'd like to have a similar design and colours to our website:
www.altaroutfitters.com.au
If possible would like the front to incorporate our information and logo and the back to have two faded example pictures of our wedding ceremonies.
I have attached two photos and our logo. Please let me know if you need a better pic of our logo though.

Target Market(s)

Newly engaged couples, aged 25 and upwards

Industry/Entity Type

Wedding

Contact Information for Business Card

Altar Outfitters
Mira Tolson
0412 871 964
altaroutfitters@mailbox-example.com
www.socialpage-example.com/AltarOutfitters

```html
<!DOCTYPE html>
<html lang="en">
<head>
<meta charset="utf-8">
<title>Altar Outfitters – Business Card</title>
<link rel="stylesheet" href="https://fonts.googleapis.com/css2?family=Alegreya:ital,wght@0,400;1,400&display=swap">
<style>
  :root {
    --page: #ffffff;
    --mint: #5ef07a;
    --charcoal: #1f2426;
    --ink: #1a1a1a;
    --light: #ffffff;
    --swirl: rgba(255, 255, 255, 0.18);
  }
  * { margin: 0; padding: 0; box-sizing: border-box; }
  html, body {
    width: 1200px;
    height: 741px;
    overflow: hidden;
    background: var(--page);
  }
  .canvas {
    position: relative;
    width: 1200px;
    height: 741px;
  }
  .card {
    position: absolute;
    left: 131px;
    top: 83px;
    width: 949px;
    height: 581px;
    overflow: hidden;
    font-family: "Alegreya", Georgia, serif;
  }
  .card__top {
    position: absolute;
    inset: 0 0 auto 0;
    height: 353px;
    background: var(--mint);
  }
  .card__bottom {
    position: absolute;
    inset: 353px 0 0 0;
    background: var(--charcoal);
  }
  .card__ornament {
    position: absolute;
    left: 0;
    top: 40px;
    width: 520px;
    height: 541px;
    background: radial-gradient(ellipse at 45% 50%, var(--swirl) 0%, rgba(255,255,255,0.08) 45%, rgba(255,255,255,0) 72%);
  }
  .brand {
    position: absolute;
    left: 60px;
    top: 48px;
    font-size: 54px;
    font-weight: 400;
    color: var(--ink);
    letter-spacing: 1px;
  }
  .tagline {
    position: absolute;
    left: 63px;
    top: 196px;
    font-style: italic;
    font-size: 22px;
    line-height: 31px;
    color: var(--ink);
  }
  .contact {
    position: absolute;
    left: 518px;
    top: 370px;
    width: 406px;
    text-align: center;
    color: var(--light);
    font-style: italic;
  }
  .contact__name {
    font-size: 27px;
    line-height: 36px;
    padding-bottom: 8px;
    border-bottom: 3px solid var(--mint);
    margin-bottom: 8px;
  }
  .contact__line {
    font-size: 21px;
    line-height: 30px;
  }
  .links {
    position: absolute;
    left: 16px;
    top: 523px;
    font-style: italic;
    font-size: 21px;
    line-height: 24px;
    color: var(--light);
  }
  .links__url { color: var(--mint); }
</style>
</head>
<body>
<div class="canvas">
  <section class="card">
    <div class="card__top"></div>
    <div class="card__bottom"></div>
    <div class="card__ornament" role="img" aria-label="Faint floral swirl ornament running across both bands"></div>

    <h1 class="brand">Altar Outfitters</h1>
    <p class="tagline">We pride ourselves on our friendly but professional services<br>in ensuring your special day is just as you imagined it to be.</p>

    <div class="contact">
      <p class="contact__name">Mira Tolson</p>
      <p class="contact__line">Phone: 0412 871 964</p>
      <p class="contact__line">Email: altaroutfitters@mailbox-example.com</p>
    </div>

    <div class="links">
      <p>Visit our Website: <span class="links__url">www.altaroutfitters.com.au</span></p>
      <p>Our Social Page: <span class="links__url">www.socialpage-example.com/AltarOutfitters</span></p>
    </div>
  </section>
</div>
</body>
</html>
```